Landing Page for Church Launch

We are a new Christian Church Plant in Milwaukee Wisconsin. I would like an exciting and unique landing page for people who are interested in:
1) What our ministry is about
2) When our ministry will be launching
3) Those who may want to join our launch team
4) Those who may want give financially into our vision
5) Those who want to follow us and get more information about us
I would also love for our color scheme to be reflective of our logo.
I included more detailed instructions and what we are looking for in the enclosed document
Religious/Christian

```html
<!DOCTYPE html>
<html lang="en">
<head>
<meta charset="utf-8">
<title>Renew Church – Launching Soon</title>
<link href="https://fonts.googleapis.com/css2?family=Lexend:wght@400;500;600&family=Roboto:wght@400;500;700&display=swap" rel="stylesheet">
<style>
:root{
  --navy:#0d0f6e;
  --navy-deep:#14106a;
  --red:#c8161d;
  --red-dark:#a80f16;
  --ink:#1d1d1f;
  --grey:#6d6d72;
  --pale:#f2f0f2;
  --pink:#f4e6e8;
  --footer:#121214;
  --white:#ffffff;
}
*{box-sizing:border-box;margin:0;padding:0}
html,body{width:1200px;height:5259px;overflow:hidden;background:var(--white)}
body{font-family:'Roboto',sans-serif;color:var(--ink)}
.page{position:relative;width:1200px;height:5259px;overflow:hidden}
.abs{position:absolute}
.heading{position:absolute;left:0;width:1200px;text-align:center;font-family:'Lexend',sans-serif;font-weight:500;font-size:30px;letter-spacing:.5px;color:var(--ink)}
.heading .mark{display:inline-block;width:10px;height:10px;background:var(--red);margin-right:12px;vertical-align:middle}
.btn{position:absolute;width:200px;height:44px;display:flex;align-items:center;justify-content:center;color:var(--white);font-size:12px;font-weight:700;letter-spacing:.3px;border-radius:2px}
.btn-red{background:var(--red)}
.btn-navy{background:var(--navy)}

/* hero */
.hero{position:absolute;left:0;top:0;width:1200px;height:720px;background:linear-gradient(180deg,#f6ece4 0%,#f3d6bf 25%,#d9a48a 45%,#8e6f8f 65%,#4e4f88 85%,#3b3f80 100%)}
.hero-photo{position:absolute;inset:0;background:radial-gradient(ellipse at 58% 52%,rgba(255,226,170,.85) 0%,rgba(255,200,140,.3) 25%,rgba(0,0,0,0) 50%)}
.brand{position:absolute;top:100px;left:0;width:1200px;text-align:center}
.brand-name{font-family:'Lexend',sans-serif;font-weight:600;font-size:40px;color:var(--red);letter-spacing:1px;line-height:1}
.hero-eyebrow{position:absolute;left:0;width:1200px;text-align:center;font-family:'Lexend',sans-serif;font-size:15px;color:var(--navy);letter-spacing:.8px}
.hero-date{position:absolute;top:230px;left:0;width:1200px;text-align:center;font-family:'Lexend',sans-serif;font-size:40px;font-weight:500;color:var(--red)}
.countdown{position:absolute;top:336px;left:468px;display:flex;gap:20px}
.count{width:53px;text-align:center}
.count-num{height:48px;background:var(--navy);color:var(--white);font-family:'Lexend',sans-serif;font-size:19px;display:flex;align-items:center;justify-content:center}
.count-label{font-size:9px;color:var(--navy);margin-top:6px}

/* mission */
.mv-panels{position:absolute;left:0;top:808px;width:1200px;height:385px}
.mv-title{position:absolute;font-family:'Lexend',sans-serif;font-weight:500;font-size:34px;color:var(--white);text-align:center}
.mv-text{position:absolute;font-size:17px;font-weight:500;line-height:30px;color:var(--white);text-align:center}

/* launch */
.lead{position:absolute;left:255px;top:1306px;width:690px;text-align:center;font-size:13.5px;line-height:26px;color:var(--grey)}
.pastor-photo{position:absolute;left:108px;top:1418px;width:482px;height:662px;background:linear-gradient(180deg,#e8ebee 0%,#c9cfd6 40%,#6c6a78 70%,#3d3b48 100%);box-shadow:0 0 14px rgba(0,0,0,.15);border-bottom:14px solid #e4e4ea}
.checks{position:absolute;left:636px;top:1428px;list-style:none;width:470px}
.checks li{font-size:13px;color:var(--grey);height:34px;display:flex;align-items:center}
.checks li svg{margin-right:12px;flex:none}
.body-text{position:absolute;left:636px;width:454px;font-size:13px;line-height:26px;color:var(--grey)}
.sub{position:absolute;left:636px;font-size:14px;font-weight:700;color:var(--ink)}

/* core values */
.values{position:absolute;left:0;top:2190px;width:1200px;height:988px;background:linear-gradient(180deg,#f7f6f8,#ecebee 50%,#f5f4f6)}
.value-icon{position:absolute;width:184px;height:140px;background:var(--pink);box-shadow:0 2px 8px rgba(0,0,0,.06)}
.value-label{position:absolute;width:300px;text-align:center;font-size:15px;color:var(--ink)}
.ring{position:absolute;left:412px;top:2540px;width:388px;height:388px;border-radius:50%;background:var(--navy);display:flex;align-items:center;justify-content:center}
.ring-inner{width:262px;height:262px;border-radius:50%;background:var(--white);display:flex;align-items:center;justify-content:center}
.ring-name{font-family:'Lexend',sans-serif;font-weight:600;font-size:48px;color:var(--red);line-height:1}

/* why */
.reasons{position:absolute;left:108px;top:3350px;width:500px;list-style:none}
.reasons li{position:relative;padding-left:32px;font-size:13.5px;line-height:26px;color:var(--grey);margin-bottom:12px}
.reasons li svg{position:absolute;left:0;top:6px}
.video-back{position:absolute;left:680px;top:3340px;width:408px;height:380px;background:var(--pink)}
.video-frame{position:absolute;left:658px;top:3388px;width:384px;height:382px;border:2px solid var(--red)}
.video{position:absolute;left:672px;top:3352px;width:398px;height:404px;background:linear-gradient(180deg,#c8a8d8 0%,#b48cc8 35%,#6a4c88 60%,#241a3a 100%);box-shadow:0 6px 16px rgba(0,0,0,.2)}
.play{position:absolute;left:848px;top:3533px;width:44px;height:44px;border-radius:50%;background:var(--white);display:flex;align-items:center;justify-content:center}

/* community */
.community{position:absolute;left:0;top:3862px;width:1200px;height:694px;background:linear-gradient(110deg,#1a1070 0%,#3a1266 45%,#8a0e2e 75%,#c3101c 100%)}
.community-heading{color:var(--white)}
.community-text{position:absolute;left:160px;top:3990px;width:880px;text-align:center;font-size:14.5px;line-height:26px;color:var(--white)}
.slide{position:absolute;left:278px;top:4105px;width:644px;height:380px;background:linear-gradient(135deg,#d8c7b4 0%,#a88670 40%,#5e4a46 70%,#2f3a5c 100%)}

/* pastor */
.pastor-cut{position:absolute;left:110px;top:4640px;width:250px;height:380px;background:linear-gradient(180deg,#6b5548 0%,#4f5468 40%,#3a4058 100%);border-radius:110px 110px 0 0}
.roles{position:absolute;left:378px;top:4780px;width:330px;list-style:none}
.roles li{position:relative;padding-left:30px;font-size:14px;line-height:21px;color:var(--grey);margin-bottom:20px}
.roles li svg{position:absolute;left:0;top:5px}
.form{position:absolute;left:748px;top:4760px;width:340px;height:395px;background:var(--white);box-shadow:0 4px 18px rgba(0,0,0,.12)}
.form-head{height:62px;background:var(--navy);color:var(--white);font-family:'Lexend',sans-serif;font-weight:500;font-size:24px;display:flex;align-items:center;justify-content:center}
.field{margin:28px 38px 0 40px;border-bottom:1px solid #d6d6da;height:26px;font-size:10.5px;color:var(--grey)}
.submit{position:absolute;left:40px;top:316px;width:262px;height:42px;background:var(--red);color:var(--white);font-size:13px;font-weight:700;display:flex;align-items:center;justify-content:center}

/* footer */
.footer{position:absolute;left:0;top:5020px;width:1200px;height:239px;background:var(--footer)}
.contact{position:absolute;display:flex;align-items:flex-start;gap:16px;color:var(--white)}
.contact-icon{width:42px;height:42px;border-radius:50%;background:var(--red);display:flex;align-items:center;justify-content:center;flex:none}
.contact-title{font-size:16px;font-weight:700}
.contact-value{font-size:13px;margin-top:4px;line-height:18px}
.copyright{position:absolute;left:110px;top:5225px;font-size:12px;color:var(--white)}
.social{position:absolute;top:5216px;width:24px;height:24px;border-radius:50%;background:var(--red)}
</style>
</head>
<body>
<div class="page">

  <!-- Hero -->
  <section class="hero">
    <div class="hero-photo" role="img" aria-label="Person with arms outstretched on a mountain top at sunset"></div>
    <div class="brand">
      <div class="brand-name">RENEW</div>
    </div>
    <div class="hero-eyebrow" style="top:196px">WE ARE COMING</div>
    <div class="hero-date">September 10, 2023 AT 5PM</div>
    <div class="hero-eyebrow" style="top:300px;font-size:14px">REVIVAL IS COMING</div>
    <div class="countdown">
      <div class="count"><div class="count-num">221</div><div class="count-label">DAYS</div></div>
      <div class="count"><div class="count-num">06</div><div class="count-label">HOURS</div></div>
      <div class="count"><div class="count-num">56</div><div class="count-label">MINS</div></div>
      <div class="count"><div class="count-num">33</div><div class="count-label">SEC</div></div>
    </div>
    <svg class="abs" style="left:0;top:560px" width="1200" height="160" viewBox="0 0 1200 160">
      <polygon points="0,123 820,150 1200,78 1200,160 0,160" fill="#ffffff"/>
      <polygon points="820,150 1200,78 1200,160 1100,160" fill="#c8161d"/>
    </svg>
  </section>

  <!-- Mission & Vision -->
  <h2 class="heading" style="top:757px"><span class="mark"></span>MISSION AND VISION</h2>
  <svg class="mv-panels" viewBox="0 0 1200 385" role="img" aria-label="Vision and mission panels over a photo of a smiling congregation">
    <polygon points="0,5 600,82 600,322 0,385" fill="#14106a"/>
    <polygon points="600,82 1200,5 1200,385 600,322" fill="#c3161c"/>
  </svg>
  <div class="mv-title" style="left:0;width:600px;top:938px">Vision</div>
  <div class="mv-text" style="left:60px;width:480px;top:988px">A Faith Community established to connect YOU to Jesus, YOUR Purpose, and the Community YOU serve.</div>
  <div class="mv-title" style="left:600px;width:600px;top:910px">Mission</div>
  <div class="mv-text" style="left:650px;width:500px;top:961px">To be the spiritual destination of choice for those seeking to connect to Jesus in a Christ-Centered, Multi-Ethnic community that serves families with and without special needs.</div>

  <!-- Launch Team -->
  <h2 class="heading" style="top:1254px"><span class="mark"></span>LAUNCH TEAM</h2>
  <p class="lead">Renew is tentatively scheduled to reopen physical doors on September 16, 2023. In preparation for those we are called to serve, we will have a launch team to help lay the groundwork to make a lasting impact and change in our community. Some of the asks of the launch team will be:</p>
  <div class="pastor-photo" role="img" aria-label="Portrait of the pastor in a plaid blazer"></div>
  <ul class="checks">
    <li><svg width="14" height="14" viewBox="0 0 14 14"><circle cx="7" cy="7" r="7" fill="#c8161d"/><path d="M4 7.2l2 2 4-4.2" stroke="#fff" stroke-width="1.6" fill="none"/></svg>Pray for the church</li>
    <li><svg width="14" height="14" viewBox="0 0 14 14"><circle cx="7" cy="7" r="7" fill="#c8161d"/><path d="M4 7.2l2 2 4-4.2" stroke="#fff" stroke-width="1.6" fill="none"/></svg>Attend monthly launch team meetings (For Planning and Strategy)</li>
    <li><svg width="14" height="14" viewBox="0 0 14 14"><circle cx="7" cy="7" r="7" fill="#c8161d"/><path d="M4 7.2l2 2 4-4.2" stroke="#fff" stroke-width="1.6" fill="none"/></svg>Invite others to the launch team and events we host</li>
    <li><svg width="14" height="14" viewBox="0 0 14 14"><circle cx="7" cy="7" r="7" fill="#c8161d"/><path d="M4 7.2l2 2 4-4.2" stroke="#fff" stroke-width="1.6" fill="none"/></svg>Volunteer at community and networking outreach events</li>
  </ul>
  <p class="body-text" style="top:1572px">Launch team members have no obligation to stay with the ministry once it's launched. Launch Team members are willing to use their time and talents to help establish another Kingdom Destination here in the earth. We'd love for you to stay around, but we rather you follow the purpose God has put in your heart.</p>
  <div class="btn btn-red" style="left:636px;top:1714px">JOIN OUR LAUNCH TEAM</div>
  <div class="sub" style="top:1790px">Prayer Group</div>
  <p class="body-text" style="top:1820px">Pray for us as directed through email and video from Pastor Eli<br>Join our Prayer Team</p>
  <div class="btn btn-navy" style="left:636px;top:1886px">JOIN OUR PRAYER TEAM</div>
  <div class="sub" style="top:1962px">Give</div>
  <p class="body-text" style="top:1992px">Pray for us as directed through email and video from Pastor Eli<br>Join our Prayer Team</p>
  <div class="btn btn-red" style="left:636px;top:2056px;width:192px">GIVE ONLINE</div>

  <!-- Core Values -->
  <section class="values" role="img" aria-label="Faint photo of a worship gathering in a sanctuary"></section>
  <h2 class="heading" style="top:2252px"><span class="mark"></span>CORE VALUES</h2>
  <div class="value-icon" style="left:508px;top:2345px" role="img" aria-label="Icon of praying hands with a cross"></div>
  <div class="value-label" style="left:450px;top:2508px">Live with the Heart of God</div>
  <div class="value-icon" style="left:202px;top:2606px" role="img" aria-label="Icon of Jesus with open arms"></div>
  <div class="value-label" style="left:146px;top:2772px">Love with the Heart of God</div>
  <div class="value-icon" style="left:814px;top:2606px" role="img" aria-label="Icon of a praying figure"></div>
  <div class="value-label" style="left:756px;top:2772px">Give with the Heart of God</div>
  <div class="ring">
    <div class="ring-inner">
      <div class="ring-name">RENEW</div>
    </div>
  </div>
  <div class="value-icon" style="left:512px;top:2938px" role="img" aria-label="Icon of an open hand holding a cross"></div>
  <div class="value-label" style="left:455px;top:3106px">Serve with the Heart of God</div>

  <!-- Why open another church -->
  <h2 class="heading" style="top:3252px;left:-8px"><span class="mark"></span>WHY OPEN ANOTHER CHURCH?</h2>
  <ul class="reasons">
    <li><svg width="12" height="12" viewBox="0 0 14 14"><circle cx="7" cy="7" r="7" fill="#c8161d"/><path d="M4 7.2l2 2 4-4.2" stroke="#fff" stroke-width="1.6" fill="none"/></svg>76% of people in the Milwaukee Metropolitan Area are not part of a faith community. There has to be an organization that addresses the needs of the people in this community.</li>
    <li><svg width="12" height="12" viewBox="0 0 14 14"><circle cx="7" cy="7" r="7" fill="#c8161d"/><path d="M4 7.2l2 2 4-4.2" stroke="#fff" stroke-width="1.6" fill="none"/></svg>Milwaukee is known as one of the most segregated big cities in the United States. What better way to begin to break ground towards unity than by creating a worship space that reflects heaven?</li>
    <li><svg width="12" height="12" viewBox="0 0 14 14"><circle cx="7" cy="7" r="7" fill="#c8161d"/><path d="M4 7.2l2 2 4-4.2" stroke="#fff" stroke-width="1.6" fill="none"/></svg>Research shows only 10 percent of people who have a child with special needs are part of a faith community. We must address the physical and mental needs of families who have children with disabilities, showering them with the love of God and the support of a like-minded community</li>
    <li><svg width="12" height="12" viewBox="0 0 14 14"><circle cx="7" cy="7" r="7" fill="#c8161d"/><path d="M4 7.2l2 2 4-4.2" stroke="#fff" stroke-width="1.6" fill="none"/></svg>Have you ever asked Why am I Here? What is my Purpose? If so, you are not alone. We help people find their purpose and connect them back to the community they serve.</li>
  </ul>
  <div class="video-back"></div>
  <div class="video-frame"></div>
  <div class="video" role="img" aria-label="Video still of worshippers raising hands beneath a cross"></div>
  <div class="play"><svg width="16" height="16" viewBox="0 0 16 16"><path d="M5 3l8 5-8 5z" fill="#1d1d1f"/></svg></div>

  <!-- Community -->
  <section class="community"></section>
  <h2 class="heading community-heading" style="top:3938px"><span class="mark"></span>COMMUNITY INVOLVEMENT</h2>
  <p class="community-text">We are looking to partner with organizations that are making a difference in our community. If you are an organization which serves families with special needs, are focused on helping people develop in purpose, or helping to meet some of the basic needs of our community, we would love to explore collaboration and partnership to serve families.</p>
  <div class="slide" role="img" aria-label="Photo of friends laughing together on a couch with open Bibles"></div>
  <svg class="abs" style="left:215px;top:4268px" width="36" height="60" viewBox="0 0 36 60"><path d="M30 4L6 30l24 26" stroke="#fff" stroke-width="4" fill="none"/></svg>
  <svg class="abs" style="left:948px;top:4268px" width="36" height="60" viewBox="0 0 36 60"><path d="M6 4l24 26L6 56" stroke="#fff" stroke-width="4" fill="none"/></svg>

  <!-- Pastor -->
  <div class="pastor-cut" role="img" aria-label="Cut-out portrait of the pastor in a suit"></div>
  <h2 class="heading" style="left:352px;width:auto;top:4712px;text-align:left"><span class="mark"></span>PASTOR ELI</h2>
  <ul class="roles">
    <li><svg width="14" height="12" viewBox="0 0 14 12"><path d="M1 1l5 5-5 5M7 1l5 5-5 5" stroke="#1d1d1f" stroke-width="2" fill="none"/></svg>Pastor</li>
    <li><svg width="14" height="12" viewBox="0 0 14 12"><path d="M1 1l5 5-5 5M7 1l5 5-5 5" stroke="#1d1d1f" stroke-width="2" fill="none"/></svg>Teacher</li>
    <li><svg width="14" height="12" viewBox="0 0 14 12"><path d="M1 1l5 5-5 5M7 1l5 5-5 5" stroke="#1d1d1f" stroke-width="2" fill="none"/></svg>Husband</li>
    <li><svg width="14" height="12" viewBox="0 0 14 12"><path d="M1 1l5 5-5 5M7 1l5 5-5 5" stroke="#1d1d1f" stroke-width="2" fill="none"/></svg>Father of a Special Needs Child who is committed to your family's Spiritual Growth and Development</li>
  </ul>

  <!-- Footer -->
  <footer class="footer"></footer>
  <div class="contact" style="left:110px;top:5064px">
    <div class="contact-icon"><svg width="20" height="14" viewBox="0 0 20 14"><rect x="1" y="1" width="18" height="12" fill="none" stroke="#fff" stroke-width="1.6"/><path d="M1 1l9 7 9-7" stroke="#fff" stroke-width="1.6" fill="none"/></svg></div>
    <div><div class="contact-title">Email Address</div><div class="contact-value">info@renewcommunity.org</div></div>
  </div>
  <div class="contact" style="left:392px;top:5064px">
    <div class="contact-icon"><svg width="18" height="18" viewBox="0 0 24 24"><path d="M6.6 10.8a15 15 0 006.6 6.6l2.2-2.2a1 1 0 011-.25 11.4 11.4 0 003.6.57 1 1 0 011 1V20a1 1 0 01-1 1A17 17 0 013 4a1 1 0 011-1h3.5a1 1 0 011 1c0 1.25.2 2.45.57 3.6a1 1 0 01-.25 1z" fill="#fff"/></svg></div>
    <div><div class="contact-title">Contact Number</div><div class="contact-value">414-555-0190</div></div>
  </div>
  <div class="contact" style="left:110px;top:5144px">
    <div class="contact-icon"><svg width="20" height="20" viewBox="0 0 20 20"><circle cx="10" cy="10" r="8" fill="none" stroke="#fff" stroke-width="1.5"/><ellipse cx="10" cy="10" rx="3.5" ry="8" fill="none" stroke="#fff" stroke-width="1.5"/><path d="M2 10h16" stroke="#fff" stroke-width="1.5"/></svg></div>
    <div><div class="contact-title">Website</div><div class="contact-value">www.renewcommunity.org</div></div>
  </div>
  <div class="contact" style="left:392px;top:5144px">
    <div class="contact-icon"><svg width="16" height="20" viewBox="0 0 16 20"><path d="M8 1a6 6 0 00-6 6c0 4.5 6 12 6 12s6-7.5 6-12a6 6 0 00-6-6z" fill="#fff"/><circle cx="8" cy="7" r="2.3" fill="#c8161d"/></svg></div>
    <div><div class="contact-value" style="margin-top:4px">Renew Church,<br>Milwaukee Wisconsin.</div></div>
  </div>
  <div class="copyright">© Copyright 2023 Renew Church | All Rights Reserved.</div>
  <div class="social" style="left:998px"></div>
  <div class="social" style="left:1031px"></div>
  <div class="social" style="left:1064px"></div>

  <!-- Contact form -->
  <form class="form">
    <div class="form-head">REACH OUT US</div>
    <div class="field">First Name</div>
    <div class="field">Last Name</div>
    <div class="field">Contact Number</div>
    <div class="field">Email Address</div>
    <div class="submit">SUBMIT NOW</div>
  </form>

</div>
</body>
</html>
```